Venture Wreckers Book Needs a Cover Design

We need a cover design for Venture Wreckers, Practical Guidance for Faltering Ventures and Doubting Company Founders. We will publish and ebook first (first priority), followed by a hard cover printed book, and then a soft cover book after a few months. The book includes 40 Venture Wreckers and actions owners can implement to counter them and grow. Some examples of killers: self-sabotage, wild optimism, scamming, addictions, burnout, no plan, procrastination, recklessness, haemorrhaging money, etc. We plan to publish the ebook to Pagelume / Tarvelo standards. We want to see designs that convey professionalism, simplicity and creativity.

Target Market(s)

Small and microbusinesses, including start-ups, proprietorships, cottage industries, home-based, single operator, and businesses with or without employees, including corporations and partnerships with fewer than five employees

Industry/Entity Type

Business

Font styles to use
Sans Serif

Colors

Designer to choose colors to be used in the design.

Requirements
Must have
• Uncluttered, professional
• Title: Venture Wreckers
• Subtitle: Practical Guidance for Faltering Ventures and Doubting Company Founders
• Author: Mel Hartigan
Nice to have
• n/a

```html
<!DOCTYPE html>
<html lang="en">
<head>
<meta charset="utf-8">
<title>Venture Wreckers — Book Cover</title>
<link rel="stylesheet" href="https://fonts.googleapis.com/css2?family=Playfair+Display:wght@900&family=Marcellus&display=swap">
<style>
  :root {
    --page: #ffffff;
    --border: #7a7a7a;
    --sky-top: #fdd08f;
    --sky-mid: #fff1de;
    --sky-bottom: #ffffff;
    --building: #c24545;
    --building-deep: #8a3a4e;
    --window: #33204a;
    --bandage: #f6cfa8;
    --panel-top: #520307;
    --panel-bottom: #c42227;
    --title-light: #fff6a8;
    --title-warm: #fbd27a;
    --title-deep: #f29a3e;
    --cream: #fff4d6;
    --author: #fde69a;
  }
  * { margin: 0; padding: 0; box-sizing: border-box; }
  html, body {
    width: 1200px;
    height: 1200px;
    overflow: hidden;
    background: var(--page);
  }
  .canvas {
    position: relative;
    width: 1200px;
    height: 1200px;
  }
  .cover {
    position: absolute;
    left: 406px;
    top: 293px;
    width: 372px;
    height: 557px;
    border: 1px solid var(--border);
    overflow: hidden;
  }
  .cover-art {
    position: absolute;
    left: 0; top: 0;
    width: 100%;
    height: 238px;
    background: linear-gradient(to bottom, var(--sky-top) 0%, var(--sky-mid) 25%, var(--sky-bottom) 45%);
  }
  .building-art {
    position: absolute;
    left: 89px;
    top: 27px;
    width: 192px;
    height: 211px;
    background:
      radial-gradient(ellipse 70px 90px at 62% 30%, color-mix(in srgb, var(--bandage) 75%, transparent) 0%, transparent 100%),
      linear-gradient(to bottom, var(--building) 0%, var(--building-deep) 55%, color-mix(in srgb, var(--window) 70%, var(--building)) 100%);
  }
  .cover-panel {
    position: absolute;
    left: 0; top: 238px;
    width: 100%;
    height: 319px;
    background: linear-gradient(to bottom, var(--panel-top), var(--panel-bottom));
  }
  .title {
    position: absolute;
    left: 0; top: 0;
    width: 372px;
    height: 180px;
  }
  .title text {
    font-family: "Playfair Display", Georgia, serif;
    font-weight: 900;
    font-size: 74px;
  }
  .subtitle {
    position: absolute;
    left: 0; top: 179px;
    width: 100%;
    text-align: center;
    font-family: "Marcellus", Georgia, serif;
    font-size: 17.5px;
    line-height: 28px;
    color: var(--cream);
  }
  .author {
    position: absolute;
    left: 0; top: 258px;
    width: 100%;
    text-align: center;
    font-family: "Marcellus", Georgia, serif;
    font-size: 41px;
    line-height: 48px;
    color: var(--author);
    letter-spacing: 0.5px;
  }
</style>
</head>
<body>
  <main class="canvas">
    <article class="cover">
      <div class="cover-art">
        <div class="building-art" role="img" aria-label="Illustration of a red office building with dark window bands and a crack patched by two adhesive bandages"></div>
      </div>
      <section class="cover-panel">
        <svg class="title" viewBox="0 0 372 180" role="heading" aria-level="1" aria-label="Venture Wreckers">
          <defs>
            <linearGradient id="titleFill" x1="0" y1="0" x2="0" y2="1">
              <stop offset="0" stop-color="var(--title-warm)"/>
              <stop offset="0.45" stop-color="var(--title-light)"/>
              <stop offset="1" stop-color="var(--title-deep)"/>
            </linearGradient>
          </defs>
          <text x="186" y="90" text-anchor="middle" textLength="318" lengthAdjust="spacingAndGlyphs" fill="url(#titleFill)">VENTURE</text>
          <text x="186" y="165" text-anchor="middle" textLength="320" lengthAdjust="spacingAndGlyphs" fill="url(#titleFill)">WRECKERS</text>
        </svg>
        <p class="subtitle">Practical Guidance for Faltering Ventures<br>and Doubting Company Founders</p>
        <p class="author">MEL HARTIGAN</p>
      </section>
    </article>
  </main>
</body>
</html>
```